Infectious Diseases Research Laboratory Needs Business Card

We need a business card for an academic research laboratory based in Kansas City called MORVEK. The full lab name is Microbial Dose-Response/Exposure Bridging Studies Laboratory, but this does not need to be incorporated. We study novel ways to optimize the treatment of multidrug-resistant bacterial infections ("superbugs") throughout the entire biomedical research spectrum (from benchtop to bedside). The name MORVEK is not only an acronym for our lab name, but also represents our desire to make discoveries and explore the unknown (the stars, if you well). It also serves as an ode to the state of Kansas motto where we are based, ad astra per aspera ("to the stars, through difficulty").

Target Market(s)

Pharmaceutical companies, researchers

Industry/Entity Type

Pharmaceutical

Contact Information for Business Card

The business card should incorporate and complement our new logo (see uploaded files). Double-sided designs are preferred. Looking for something modern, but professional.

Font styles to use
Sans Serif

Requirements
Must have
• Double-sided. One side would ideally be a solid color incorporating logo and the other should also have the logo (smaller), but incorporate staff information.
• Color codes:
• Red: #F04C51
• Blue: #3477B5
• Gray: #808285

```html
<!DOCTYPE html>
<html lang="en">
<head>
<meta charset="utf-8">
<title>MORVEK Business Card</title>
<link href="https://fonts.googleapis.com/css2?family=Arimo:wght@400;700&family=Caladea&display=swap" rel="stylesheet">
<style>
  :root {
    --red: #F04C51;
    --blue: #3477B5;
    --gray: #808285;
    --ink: #333436;
    --paper: #ffffff;
    --backdrop: #eef1f3;
  }
  * { margin: 0; padding: 0; box-sizing: border-box; }
  html, body {
    width: 1200px; height: 965px; overflow: hidden;
    background: var(--backdrop);
  }
  .canvas { position: relative; width: 1200px; height: 965px; }
  .card {
    position: absolute; left: 275px; width: 703px; height: 388px;
  }
  .card--front { top: 87px; background: var(--paper); }
  .card--back { top: 511px; background: var(--red); }

  .brand {
    position: absolute; display: flex; align-items: center; gap: 10px;
  }
  .brand__dot { width: 22px; height: 22px; border-radius: 50%; flex: none; }
  .brand__name {
    font-family: "Arimo", sans-serif; font-weight: 400;
    font-size: 44px; letter-spacing: 2px; line-height: 1;
  }
  .brand__sub {
    position: absolute; font-family: "Arimo", sans-serif; font-size: 5.5px;
    letter-spacing: 0.3px; white-space: nowrap; text-transform: uppercase;
  }
  .card--front .brand { left: 80px; top: 133px; }
  .card--front .brand__dot { background: var(--blue); }
  .card--front .brand__name { color: var(--red); }
  .card--front .brand__sub { left: 112px; top: 182px; color: var(--gray); }

  .divider {
    position: absolute; left: 351px; top: 132px; width: 1.5px; height: 45px;
    background: var(--ink);
  }
  .person { position: absolute; left: 379px; top: 138px; font-family: "Arimo", sans-serif; }
  .person__name { font-size: 27px; font-weight: 700; color: var(--ink); line-height: 1; }
  .person__role { font-size: 17.5px; color: var(--blue); margin-top: 3px; }

  .contact {
    position: absolute; left: 0; right: 0; top: 298px;
    font-family: "Caladea", serif; font-size: 17px; color: #4a4b4d;
  }
  .contact__line { display: flex; align-items: center; gap: 9px; margin-left: 310px; height: 21px; }
  .contact__line svg { width: 13px; height: 13px; flex: none; }
  .contact__address { text-align: center; margin-top: 7px; }

  .card--back .brand { left: 50%; top: 170px; transform: translateX(-50%); gap: 14px; }
  .card--back .brand__dot { background: var(--paper); width: 30px; height: 30px; }
  .card--back .brand__name { color: var(--paper); font-size: 52px; }
  .card--back .brand__sub { left: 298px; top: 230px; color: var(--paper); }
  .website {
    position: absolute; left: 0; right: 0; top: 347px; text-align: center;
    font-family: "Arimo", sans-serif; font-size: 19.5px; color: var(--paper);
  }
</style>
</head>
<body>
<main class="canvas">
  <section class="card card--front">
    <div class="brand">
      <span class="brand__dot"></span>
      <span class="brand__name">MORVEK</span>
    </div>
    <span class="brand__sub">Microbial Dose-Response/Exposure Bridging Studies Laboratory</span>
    <span class="divider"></span>
    <div class="person">
      <p class="person__name">Dana Whitlow</p>
      <p class="person__role">Vice President</p>
    </div>
    <div class="contact">
      <p class="contact__line">
        <svg viewBox="0 0 16 16" aria-hidden="true"><path fill="#3477B5" d="M4 1.5l2.2 3-1.3 1.6a9 9 0 0 0 5 5l1.6-1.3 3 2.2-1.3 2.5C8 14.5 1.5 8 1.5 2.8z"/></svg>
        <span>001 816 5520</span>
      </p>
      <p class="contact__line">
        <svg viewBox="0 0 16 12" aria-hidden="true"><rect width="16" height="12" fill="#3477B5"/><path d="M0 0l8 6.5L16 0" fill="none" stroke="#fff" stroke-width="1.3"/></svg>
        <span>info@morvek-lab.org</span>
      </p>
      <p class="contact__address">Postal Code, Road Name, City Name, Country 64108</p>
    </div>
  </section>

  <section class="card card--back">
    <div class="brand">
      <span class="brand__dot"></span>
      <span class="brand__name">MORVEK</span>
    </div>
    <p class="website">www.morvek-lab.org</p>
  </section>
</main>
</body>
</html>
```